Flowchart

I need a nice graphic that doesn't look like a stock word/ppt graphic to show the organization of our office. Example included. The idea to get across is that all of the units work together and feed into each other. I need this asap so will likely award tomorrow
Please use all text and if possible incorporate logo.
Design should be around 8.5 X 11 or smaller. Landscape vs. Protrait doesn't matter much.
A few more notes.
no larger than 81/2 by 11
Landscape preferred
Landscape preferred
Landscape

```html
<!DOCTYPE html>
<html lang="en">
<head>
<meta charset="utf-8">
<title>Biosciences Graduate Education – Organization</title>
<link rel="stylesheet" href="https://fonts.googleapis.com/css2?family=Source+Sans+3:wght@400&display=swap">
<style>
  :root {
    --canvas-white: #ffffff;
    --sky-light: #e9f5fc;
    --sky-deep: #6cc1ec;
    --spine-dark: #1f1766;
    --spine-mid: #3a2d8e;
    --unit-blue: #0a8fd8;
    --unit-frame: #ffffff;
    --ink: #1e1e1e;
    --outline: #8a8a8a;
  }
  * { box-sizing: border-box; margin: 0; padding: 0; }
  html, body { width: 1200px; height: 815px; overflow: hidden; }
  body { font-family: "Source Sans 3", "Myriad Pro", Arial, sans-serif; background: var(--canvas-white); }

  .org-chart {
    position: relative;
    width: 1200px;
    height: 815px;
    border: 1px solid var(--outline);
    background: linear-gradient(90deg, var(--canvas-white) 0%, var(--canvas-white) 36%, var(--sky-light) 55%, var(--sky-deep) 100%);
    overflow: hidden;
  }

  .spine {
    position: absolute;
    left: 146px;
    top: 0;
    width: 171px;
    height: 100%;
    background: linear-gradient(90deg, var(--spine-dark) 0%, var(--spine-mid) 45%, var(--spine-mid) 55%, var(--spine-dark) 100%);
  }

  .unit {
    position: absolute;
    left: 59px;
    width: 346px;
    padding: 8px;
    background: var(--unit-frame);
    box-shadow: 3px 4px 8px rgba(0, 0, 0, 0.12);
  }
  .unit-box {
    height: 100%;
    background: var(--unit-blue);
    color: #fff;
    font-size: 29px;
    line-height: 1.33;
    text-align: center;
    display: flex;
    align-items: center;
    justify-content: center;
  }
  .unit--home { top: 85px; height: 145px; }
  .unit--cgap { top: 271px; height: 223px; }
  .unit--oge  { top: 535px; height: 223px; }

  .roles {
    position: absolute;
    left: 462px;
    width: 720px;
    list-style: none;
    font-size: 21px;
    line-height: 27px;
    color: var(--ink);
  }
  .roles li { position: relative; padding-left: 15px; }
  .roles li::before { content: "•"; position: absolute; left: 0; }
  .roles--home { top: 97px; }
  .roles--cgap { top: 338px; }
  .roles--oge  { top: 562px; }
</style>
</head>
<body>
<main class="org-chart">
  <div class="spine" aria-hidden="true"></div>

  <section class="unit unit--home">
    <h2 class="unit-box" style="font-weight:400">Biosciences<br>Home Programs</h2>
  </section>
  <ul class="roles roles--home">
    <li>Supports students with department or program specific degree<br>progress and graduation requirements</li>
    <li>Administers program-specific core curriculum</li>
    <li>Eight departments and Six interdisciplinary programs</li>
  </ul>

  <section class="unit unit--cgap">
    <h2 class="unit-box" style="font-weight:400">Committee on<br>Graduate<br>Admissions &amp; Policy<br>CGAP)</h2>
  </section>
  <ul class="roles roles--cgap">
    <li>Administrative oversight of Biosciences admissions, curriculum and<br>policies</li>
    <li>Forum for cross-program discussion and collaboration</li>
  </ul>

  <section class="unit unit--oge">
    <h2 class="unit-box" style="font-weight:400">Office of Graduate<br>Education (OGE) &amp;<br>School of Medicine<br>Career Center<br>(SoMCC)</h2>
  </section>
  <ul class="roles roles--oge">
    <li>Promotes the academic, personal &amp; professional development of all<br>students through comprehensive programs and services</li>
    <li>Advocates for the best possible training and empowerment of all<br>students</li>
    <li>Develops and administers Biosciences – wide, &nbsp;interdisciplinary<br>curriculum</li>
  </ul>
</main>
</body>
</html>
```